Real estate agent website

I am a new real estate agent and in of a simple but powerful website that is linked to the local Multiple listing services (MLS). It should have a lending page that is connected to my customer relationship management (CRM) software. It must have an ability for potential customers to search for properties and be able to communicate with me easily.
Updates

Updates: The website themes must includes MLS-IDX integration with a grid layout and property slider so i can showcase featured properties. I also would like to have future where potential client can search and have alerts depending on a search criteria.

Industry/Entity Type

Real Estate

Coding

Coded - Design and coding required

Number of Pages Required

3 page

Requirements
Must have
• Home page, Resources page, About Me with contact me window page

```html
<!DOCTYPE html>
<html lang="en">
<head>
<meta charset="utf-8">
<title>Real Estate Agent</title>
<link href="https://fonts.googleapis.com/css2?family=Rubik:wght@400;500;600;700;800&family=Poppins:ital,wght@0,400;0,500;0,600;1,400&display=swap" rel="stylesheet">
<style>
:root{
  --accent:#f9b233;
  --dark:#403e4a;
  --ink:#2f2d36;
  --muted:#8a8890;
  --field:#eeece6;
  --line:#dcdad4;
  --footer:#efede5;
  --white:#fff;
}
*{box-sizing:border-box;margin:0;padding:0}
html,body{width:1200px;height:4376px;overflow:hidden}
body{position:relative;background:var(--white);font-family:"Poppins",sans-serif;color:var(--ink)}
.abs{position:absolute}
h1,h2,h3{font-family:"Rubik",sans-serif}
.btn{display:inline-block;background:var(--accent);color:var(--white);font-family:"Rubik",sans-serif;font-weight:600;font-size:13px;letter-spacing:.3px;text-transform:uppercase;padding:11px 22px;border-radius:2px}
.rule{width:76px;height:2px;background:var(--line)}
.rule.light{background:rgba(255,255,255,.7)}

/* nav */
.nav{left:0;top:0;width:1200px;height:97px}
.logo{left:127px;top:40px;font-family:"Rubik",sans-serif;font-weight:600;font-size:17px;color:#6d6b72}
.menu{left:340px;top:42px;display:flex;gap:40px;font-family:"Rubik",sans-serif;font-size:14px;font-weight:500}
.menu .on{color:var(--accent)}
.nav .btn{left:935px;top:33px;font-size:11px;padding:11px 16px}

/* hero */
.hero{left:0;top:97px;width:1200px;height:656px;background:linear-gradient(110deg,#5b5550 0%,#7a6e62 35%,#8b7f70 60%,#4f5a44 100%)}
.hero::after{content:"";position:absolute;inset:0;background:rgba(30,28,34,.45)}
.hero h1{position:absolute;z-index:1;left:0;width:1200px;top:302px;text-align:center;color:var(--white);font-weight:800;font-size:40px;line-height:44px}

/* search */
.call{left:105px;top:624px;width:323px;height:223px;background:var(--dark);text-align:center;color:var(--white)}
.call svg{margin-top:42px}
.call .title{font-family:"Rubik",sans-serif;font-weight:700;font-size:31px;color:var(--accent);margin-top:10px}
.call .num{font-family:"Rubik",sans-serif;font-weight:500;font-size:20px;margin-top:2px}
.search{left:428px;top:624px;width:667px;height:223px;background:var(--white);box-shadow:0 6px 18px rgba(0,0,0,.12);padding:0 44px 0 36px}
.search h3{font-weight:500;font-size:20px;margin-top:32px;padding-bottom:14px;border-bottom:2px solid var(--line)}
.fields{display:grid;grid-template-columns:repeat(3,188px);gap:12px 12px;margin-top:24px}
.field{height:38px;background:var(--field);font-size:11px;color:#8e8c88;padding:12px 14px;position:relative}
.field.sel::after{content:"";position:absolute;right:14px;top:17px;border:4px solid transparent;border-top-color:#555}
.fields .btn{height:38px;padding:11px 0;text-align:center;font-size:14px}

/* about */
.about h2{left:151px;top:1084px;font-weight:600;font-size:37px;line-height:46px;color:var(--dark)}
.about .rule{left:151px;top:1200px}
.about .lead{left:148px;top:1224px;width:262px;font-family:"Rubik",sans-serif;font-size:18px;line-height:24px;color:var(--muted)}
.photo-agent{left:452px;top:1040px;width:296px;height:320px;background:linear-gradient(180deg,#efede2,#d9d5c8)}
.about .copy{left:794px;top:1066px;width:262px;font-size:14px;line-height:20.5px;color:#3e3c44}
.about .btn{left:804px;top:1296px}

/* properties */
.props{left:0;top:1508px;width:1200px;height:556px;background:var(--dark);overflow:hidden}
.props h2{position:absolute;left:148px;top:175px;color:var(--white);font-weight:600;font-size:34px}
.props .rule{position:absolute;left:148px;top:236px}
.props .copy{position:absolute;left:150px;top:270px;width:262px;color:var(--white);font-size:14px;line-height:20.5px}
.props .arrows{position:absolute;left:150px;top:392px}
.card{position:absolute;top:141px;width:246px;height:282px;background:var(--white)}
.card .pic{height:180px;background:linear-gradient(160deg,#e8e6e2,#b8b4ad)}
.card .tag{position:absolute;left:92px;top:166px;background:#ecebe6;font-size:10px;padding:4px 10px;color:#444}
.card .side{position:absolute;left:0;top:180px;width:36px;height:102px;border-right:1px solid #e4e2de;display:flex;flex-direction:column;align-items:center;gap:9px;padding-top:14px}
.card .name{position:absolute;left:57px;top:208px;font-family:"Rubik",sans-serif;font-weight:500;font-size:13px;line-height:16px;color:#333}
.card .meta{position:absolute;left:57px;top:254px;display:flex;gap:24px;font-size:10px;color:#999;white-space:nowrap}

/* mls */
.accent-block{left:36px;top:2176px;width:176px;height:148px;background:#e9e8e6}
.photo-mls{left:97px;top:2220px;width:440px;height:361px;background:linear-gradient(120deg,#3b3431,#a07c56 55%,#e6cfa9 75%,#6d5a48)}
.mls h2{left:593px;top:2244px;font-weight:600;font-size:36px;color:var(--dark)}
.mls .rule{left:594px;top:2313px}
.mls .copy{left:593px;top:2338px;width:462px;font-size:14px;line-height:20.5px;color:#3e3c44}
.mls .btn{left:595px;top:2525px}

/* crm */
.crm{left:0;top:2757px;width:1200px;height:517px;background:linear-gradient(100deg,#3e3630 0%,#7e6b57 40%,#b9a58b 65%,#d6c6ac 85%,#8c7762 100%)}
.bubble{left:147px;top:2855px;width:316px;height:316px;border-radius:50%;background:var(--white);text-align:center}
.bubble h2{font-weight:500;font-size:37px;line-height:44px;color:var(--dark);margin-top:60px}
.bubble .rule{margin:8px auto 0;width:96px}
.bubble p{font-size:14px;line-height:20.5px;color:#3e3c44;width:230px;margin:12px auto 0}
.bubble .btn{margin-top:12px}

/* testimonials */
.testi h2{left:0;width:1200px;top:3380px;text-align:center;font-weight:600;font-size:36px;color:var(--dark)}
.testi .rule{left:562px;top:3452px}
.quote-card{left:224px;top:3502px;width:743px;height:348px;background:var(--white);box-shadow:0 4px 20px rgba(0,0,0,.08);text-align:center}
.reviewer{font-family:"Rubik",sans-serif;font-weight:500;font-size:40px;color:#4a4a54;margin-top:40px;line-height:44px}
.stars{margin-top:2px}
.quote-card .text{width:545px;margin:28px auto 0;font-style:italic;font-size:13px;line-height:20.5px;color:#555}
.quote-card .who{margin-top:26px;font-family:"Rubik",sans-serif;font-weight:500;font-size:16px}
.qmark{left:868px;top:3468px}
.arrow-l{left:176px;top:3675px}
.arrow-r{left:993px;top:3675px}

/* footer */
.footer{left:0;top:3971px;width:1200px;height:405px;background:var(--footer)}
.footer-col h3{font-weight:600;font-size:22px;color:var(--dark)}
.f-links{left:150px;top:4042px}
.f-links ul{list-style:none;margin-top:14px;font-size:12px;line-height:22px}
.f-contact{left:342px;top:4042px}
.f-contact .row{display:flex;gap:12px;align-items:flex-start;font-size:12px;line-height:17px;margin-top:12px}
.ic{width:29px;height:29px;flex:none;background:var(--dark);border-radius:3px;display:flex;align-items:center;justify-content:center}
.f-divider{left:655px;top:4054px;width:1px;height:145px;background:#bdbab2}
.f-news{left:750px;top:4042px;width:302px}
.f-news p{font-size:12px;line-height:15px;margin-top:14px}
.email{margin-top:14px;height:41px;border:1px solid #888;background:var(--white);font-size:12px;padding:12px 8px;position:relative}
.email svg{position:absolute;right:14px;top:10px}
.f-rule{left:150px;top:4268px;width:900px;height:1px;background:#8c8a84}
.copyright{left:0;width:1200px;top:4290px;text-align:center;font-size:14px}
</style>
</head>
<body>

<header class="abs nav">
  <div class="abs logo">Logo Name</div>
  <nav class="abs menu"><span class="on">Home</span><span>Our Story</span><span>Our Team</span><span>Properties</span><span>Blog</span><span>Reviews</span></nav>
  <span class="abs btn">Request a quote</span>
</header>

<section class="abs hero" role="img" aria-label="Photo of a young couple reviewing documents with an agent">
  <h1>Lorem ipsum dolor sit amet,<br>consectetur adipiscing.</h1>
</section>

<div class="abs call">
  <svg width="52" height="52" viewBox="0 0 52 52" fill="none" stroke="#fff" stroke-width="2.4" stroke-linecap="round">
    <path d="M14 6l7 9-4 5c2 5 7 10 12 12l5-4 9 7-4 6c-14 1-30-15-30-29z"/>
    <path d="M30 8a14 14 0 0 1 14 14" stroke="#f9b233"/><path d="M30 15a7 7 0 0 1 7 7" stroke="#f9b233"/>
  </svg>
  <div class="title">Call Us Now</div>
  <div class="num">+1 555 014 2290</div>
</div>
<div class="abs search">
  <h3>Find a Property</h3>
  <div class="fields">
    <div class="field">Filter by Keywords</div>
    <div class="field sel">Type of House</div>
    <div class="field sel">City</div>
    <div class="field sel">No.of beds</div>
    <div class="field sel">Price Range</div>
    <span class="btn">Find Property</span>
  </div>
</div>

<section class="about">
  <h2 class="abs">About Real<br>Estate Agent</h2>
  <div class="abs rule"></div>
  <p class="abs lead">Lorem ipsum dolor sit amet, consec tetur adipiscing elit, sed do eiusmod loytempor incididunt ut labor</p>
  <div class="abs photo-agent" role="img" aria-label="Portrait of the real estate agent holding a tablet"></div>
  <p class="abs copy">Lorem ipsum dolor sit amet, consec tetur adipiscing elit, sed do eiusmod tempor incididunt ut labore et dolore magna aliqua. Quis ipsum suspendis se ultrices gravida. Risus commodo viverra maecenas accumsan lacus vel facilisis. unt ut labore et dolore magna aliqua. Quis ipsum suspendis se ultrices gravida. Risus commodo viverra maecenas ac</p>
  <span class="abs btn">Read more</span>
</section>

<section class="abs props">
  <h2>Our Properties</h2>
  <div class="rule light"></div>
  <p class="copy">Lorem ipsum dolor sit amet, consec tetur adipiscing elit, sed do eiusmod tempor incididunt ut labore et dolore magna aliqua. Quis ipsum suspendis se ultrices</p>
  <svg class="arrows" width="24" height="16" viewBox="0 0 24 16" fill="none" stroke="#fff" stroke-width="2.2"><path d="M8 2L2 8l6 6M16 2l6 6-6 6"/></svg>

  <div class="card" style="left:483px">
    <div class="pic" role="img" aria-label="Interior photo of a staircase and hallway"></div>
    <span class="tag">For Rent</span>
    <div class="side">
      <svg width="16" height="12" viewBox="0 0 16 12" fill="none" stroke="#666" stroke-width="1.3"><path d="M1 6s3-5 7-5 7 5 7 5-3 5-7 5-7-5-7-5z"/><circle cx="8" cy="6" r="2"/></svg>
      <svg width="14" height="13" viewBox="0 0 14 13" fill="none" stroke="#666" stroke-width="1.3"><path d="M7 12S1 8 1 4a3 3 0 0 1 6-1 3 3 0 0 1 6 1c0 4-6 8-6 8z"/></svg>
      <svg width="12" height="16" viewBox="0 0 12 16" fill="none" stroke="#666" stroke-width="1.3"><path d="M6 15S1 9 1 6a5 5 0 0 1 10 0c0 3-5 9-5 9z"/><circle cx="6" cy="6" r="2"/></svg>
    </div>
    <div class="name">Lorem ipsum dolor loesit<br>amet, consectetur.</div>
    <div class="meta"><span>3 beds</span><span>2 bath</span><span>1000 sq ft</span></div>
  </div>
  <div class="card" style="left:763px">
    <div class="pic" role="img" aria-label="Interior photo of a modern kitchen"></div>
    <span class="tag">For Rent</span>
    <div class="side">
      <svg width="16" height="12" viewBox="0 0 16 12" fill="none" stroke="#666" stroke-width="1.3"><path d="M1 6s3-5 7-5 7 5 7 5-3 5-7 5-7-5-7-5z"/><circle cx="8" cy="6" r="2"/></svg>
      <svg width="14" height="13" viewBox="0 0 14 13" fill="none" stroke="#666" stroke-width="1.3"><path d="M7 12S1 8 1 4a3 3 0 0 1 6-1 3 3 0 0 1 6 1c0 4-6 8-6 8z"/></svg>
      <svg width="12" height="16" viewBox="0 0 12 16" fill="none" stroke="#666" stroke-width="1.3"><path d="M6 15S1 9 1 6a5 5 0 0 1 10 0c0 3-5 9-5 9z"/><circle cx="6" cy="6" r="2"/></svg>
    </div>
    <div class="name">Lorem ipsum dolor loesit<br>amet, consectetur.</div>
    <div class="meta"><span>3 beds</span><span>2 bath</span><span>1000 sq ft</span></div>
  </div>
  <div class="card" style="left:1035px">
    <div class="pic" role="img" aria-label="Interior photo of an open dining area"></div>
    <span class="tag">For Rent</span>
    <div class="side">
      <svg width="16" height="12" viewBox="0 0 16 12" fill="none" stroke="#666" stroke-width="1.3"><path d="M1 6s3-5 7-5 7 5 7 5-3 5-7 5-7-5-7-5z"/><circle cx="8" cy="6" r="2"/></svg>
      <svg width="14" height="13" viewBox="0 0 14 13" fill="none" stroke="#666" stroke-width="1.3"><path d="M7 12S1 8 1 4a3 3 0 0 1 6-1 3 3 0 0 1 6 1c0 4-6 8-6 8z"/></svg>
      <svg width="12" height="16" viewBox="0 0 12 16" fill="none" stroke="#666" stroke-width="1.3"><path d="M6 15S1 9 1 6a5 5 0 0 1 10 0c0 3-5 9-5 9z"/><circle cx="6" cy="6" r="2"/></svg>
    </div>
    <div class="name">Lorem ipsum dolor loesit<br>amet, consectetur.</div>
    <div class="meta"><span>3 beds</span><span>2 bath</span><span>1000 sq ft</span></div>
  </div>
</section>

<section class="mls">
  <div class="abs accent-block" role="img" aria-label="Decorative accent behind the photo"></div>
  <div class="abs photo-mls" role="img" aria-label="Photo of an agent signing papers beside a small model house"></div>
  <h2 class="abs">Multiple listing services</h2>
  <div class="abs rule"></div>
  <p class="abs copy">Lorem ipsum dolor sit amet, consec tetur adipiscing elit, sed do eiusmod tempor incididunt ut labore et dolore magna aliqualouis ipsum suspendisse ultrices gravida. Risus commodo viverra mae cenas accumsan lacus vel facilisis. unt ut labore et dolore lorem is magna aliqua. Quis ipsum suspendisse ultrices gravidaisus comm odo viverra maecena gravida. Risus commodo viverra mae cenas accumsan lacus vel facilisis. unt ut labore et dolore lorem is magna aliqua. Quis ipsum suspends ac</p>
  <span class="abs btn">Read more</span>
</section>

<section class="abs crm" role="img" aria-label="Photo of a laptop and coffee cup on a wooden desk"></section>
<div class="abs bubble">
  <h2>(CRM)<br>Software</h2>
  <div class="rule"></div>
  <p>Lorem ipsum dolor sit amet con sec tetur adipiscing elit, sed do eiusmod tempor incididun.</p>
  <span class="btn">Read more</span>
</div>

<section class="testi">
  <h2 class="abs">Client Testimonials</h2>
  <div class="abs rule"></div>
  <div class="abs quote-card">
    <div class="reviewer">Reviewly</div>
    <svg class="stars" width="104" height="18" viewBox="0 0 104 18" fill="#f9b233">
      <g id="star"><path d="M9 1l2.4 5.2 5.6.6-4.2 3.8 1.2 5.6L9 13.4 4 16.2l1.2-5.6L1 6.8l5.6-.6z"/></g>
      <use href="#star" x="21"/><use href="#star" x="42"/><use href="#star" x="63"/><use href="#star" x="84"/>
    </svg>
    <p class="text">Lorem ipsum dolor sit amet, consectetur adipiscing elit, sed do eiusmod tempor incididunt ut labore et dolore magna aliqua. Quis ipsum suspendisse ultrices gravida. Risus commodo viverra maecenas accumsan lacus ve do eiusmod tempor incididunt ut labore et dolore magna aliqua. Quis ipsum suspendisse ultrices gravida. Risus commodo viverra maecenas accumsan lacus vel facilisis.</p>
    <div class="who">Dana Whitfield</div>
  </div>
  <svg class="abs qmark" width="80" height="56" viewBox="0 0 80 56" fill="#2a2a2e"><circle cx="17" cy="17" r="15"/><path d="M30 20c0 18-10 30-26 34l-1-5c10-4 15-12 15-22z"/><circle cx="57" cy="17" r="15"/><path d="M70 20c0 18-10 30-26 34l-1-5c10-4 15-12 15-22z"/></svg>
  <svg class="abs arrow-l" width="32" height="18" viewBox="0 0 32 18" fill="none" stroke="#222" stroke-width="3"><path d="M31 9H3M10 2L3 9l7 7"/></svg>
  <svg class="abs arrow-r" width="32" height="18" viewBox="0 0 32 18" fill="none" stroke="#222" stroke-width="3"><path d="M1 9h28M22 2l7 7-7 7"/></svg>
</section>

<footer class="abs footer"></footer>
<div class="abs footer-col f-links">
  <h3>Links</h3>
  <ul><li>About Us</li><li>Our Story</li><li>Our Team</li><li>Properties</li><li>Blog</li><li>Reviews</li></ul>
</div>
<div class="abs footer-col f-contact">
  <h3>Contact</h3>
  <div class="row"><span class="ic"><svg width="10" height="14" viewBox="0 0 12 16" fill="#fff"><path d="M6 15S1 9 1 6a5 5 0 0 1 10 0c0 3-5 9-5 9z"/><circle cx="6" cy="6" r="2" fill="#403e4a"/></svg></span><span>Address:&nbsp; 48 Maple Row, Suite 12<br>Harbor City 40210</span></div>
  <div class="row"><span class="ic"><svg width="13" height="10" viewBox="0 0 13 10" fill="#fff"><rect width="13" height="10" rx="1"/><path d="M1 1l5.5 4.5L12 1" stroke="#403e4a" fill="none"/></svg></span><span style="padding-top:6px">Email: hello@harborkeys.com</span></div>
  <div class="row"><span class="ic"><svg width="12" height="12" viewBox="0 0 52 52" fill="#fff"><path d="M14 6l7 9-4 5c2 5 7 10 12 12l5-4 9 7-4 6c-14 1-30-15-30-29z"/></svg></span><span style="padding-top:6px">Phone: 555 014 2290</span></div>
</div>
<div class="abs f-divider"></div>
<div class="abs footer-col f-news">
  <h3>Newsletter</h3>
  <p>Lorem ipsum dolor sit amet, consectetur adipi scing elit, sed do eiusmod tempo</p>
  <div class="email">Email:
    <svg width="22" height="20" viewBox="0 0 22 20" fill="#222"><path d="M21 1L1 9l6 2 2 7 3-5 5 4z"/></svg>
  </div>
</div>
<div class="abs f-rule"></div>
<div class="abs copyright">Copyrights © 2023 Company Name. All rights Reserved</div>

</body>
</html>
```